Flyer

I am a qualified accountant and I need a flyer to promote my business when networking

My services include
Management Accounts, Financial Accounts, Day to Day Bookkeeping services, business start up assistance
I will produce and submit Self Assessment Tax Returns, Annual Accounts, VAT tax returns, Payroll and PAYE

I attach my business card design so that there is some continuity if you think it appropiate.

Size A3 is preferred, please.

Sorry, I mean't Size A5 is preferred.

A5 please

Free initial consultations and advice.

```html
<!DOCTYPE html>
<html lang="en">
<head>
<meta charset="utf-8">
<title>Clara Moss Accounting – Flyer</title>
<link rel="stylesheet" href="https://fonts.googleapis.com/css2?family=Noto+Sans:ital,wght@0,400;1,400&display=swap">
<style>
  :root {
    --green-bright: #74e03c;
    --green-olive: #8ec84b;
    --banner-lime: #c6dc3c;
    --navy: #0d1a4d;
    --ink: #17184a;
    --burst-red: #d5434c;
  }
  * { margin: 0; padding: 0; box-sizing: border-box; }
  html, body { width: 1200px; height: 2596px; overflow: hidden; }
  body { font-family: "Noto Sans", Arial, sans-serif; color: var(--ink); background: var(--green-bright); }
  .flyer { position: relative; width: 1200px; height: 2596px; background: var(--green-bright); }
  .services-panel { position: absolute; left: 0; top: 975px; width: 1200px; height: 1558px; background: var(--green-olive); border-top: 2px solid #a6d874; }

  .banner { position: absolute; left: 257px; top: 87px; width: 672px; height: 173px; background: var(--banner-lime); display: flex; align-items: center; padding-left: 55px; font-size: 43px; letter-spacing: 0.5px; }
  .banner-tails { position: absolute; left: 0; top: 0; }

  .tagline, .credentials, .contact { position: absolute; font-size: 44px; line-height: 1; }
  .tagline { left: 312px; top: 422px; }
  .credentials { left: 312px; top: 532px; }
  .contact.email { left: 343px; top: 698px; }
  .contact.phone { left: 346px; top: 874px; }
  .icon { position: absolute; }

  .services-title { position: absolute; left: 144px; top: 1016px; width: 817px; height: 87px; background: var(--green-bright); font-style: italic; font-size: 44px; display: flex; align-items: center; padding-left: 6px; }

  .service { position: absolute; left: 179px; background: var(--green-bright); font-size: 44px; line-height: 1.25; display: flex; align-items: center; padding-left: 26px; }
  .service.multi { align-items: flex-start; padding-top: 20px; line-height: 1.2; }

  .offer-burst { position: absolute; left: 820px; top: 1160px; }
  .offer-text { position: absolute; left: 860px; top: 1218px; color: var(--ink); }
  .offer-text .big { font-size: 63px; line-height: 1; display: block; }
  .offer-text .small { font-size: 27px; line-height: 1.03; display: block; margin-top: 6px; }
</style>
</head>
<body>
<main class="flyer">
  <svg class="banner-tails" width="1200" height="400" aria-hidden="true">
    <polygon points="257,258 366,258 366,375" fill="var(--navy)"/>
    <polygon points="825,258 929,258 825,375" fill="var(--navy)"/>
  </svg>
  <h1 class="banner" style="font-weight:400">CLARA MOSS ACCOUNTING</h1>

  <p class="tagline">Making Accounts look easy</p>
  <p class="credentials">Clara Moss ACMA, CGMA</p>

  <svg class="icon" style="left:146px;top:680px" width="90" height="90" viewBox="0 0 90 90" aria-hidden="true">
    <g transform="rotate(-32 45 45)">
      <rect x="10" y="22" width="70" height="46" fill="var(--navy)"/>
      <polyline points="10,22 45,50 80,22" fill="none" stroke="var(--green-bright)" stroke-width="4"/>
    </g>
  </svg>
  <p class="contact email">clara@claramossaccounting.com</p>

  <svg class="icon" style="left:150px;top:842px" width="76" height="76" viewBox="0 0 76 76" aria-hidden="true">
    <rect width="76" height="76" rx="12" fill="var(--navy)"/>
    <path d="M24 16 l10 0 l4 14 l-7 5 q5 10 14 14 l5 -7 l14 4 l0 10 q-3 5 -10 5 q-34 -6 -38 -38 q0 -6 8 -7z" fill="var(--green-bright)"/>
  </svg>
  <p class="contact phone">07700 900123</p>

  <section class="services-panel"></section>

  <h2 class="services-title" style="font-weight:400">Services of a Qualified accountant</h2>

  <div class="service" style="top:1142px;width:591px;height:87px">Management Accounting,</div>
  <div class="service" style="top:1261px;width:591px;height:87px">Financial Accounting,</div>
  <div class="service" style="top:1393px;width:591px;height:81px">Budgeting,</div>
  <div class="service" style="top:1518px;width:744px;height:87px">Day to Day Bookkeeping Services</div>
  <div class="service multi" style="top:1665px;width:744px;height:156px">Production and submission of<br>Self Assessment Tax Returns</div>
  <div class="service" style="top:1884px;width:580px;height:118px">VAT returns,</div>
  <div class="service" style="top:2057px;width:580px;height:118px">Annual Accounts,</div>
  <div class="service" style="top:2218px;width:572px;height:118px">Payroll &amp; PAYE</div>
  <div class="service" style="top:2392px;width:577px;height:115px">Business start up assistance</div>

  <svg class="offer-burst" width="276" height="276" viewBox="-138 -138 276 276" aria-hidden="true">
    <g fill="var(--burst-red)">
      <rect x="-97" y="-97" width="194" height="194"/>
      <rect x="-97" y="-97" width="194" height="194" transform="rotate(15)"/>
      <rect x="-97" y="-97" width="194" height="194" transform="rotate(30)"/>
      <rect x="-97" y="-97" width="194" height="194" transform="rotate(45)"/>
      <rect x="-97" y="-97" width="194" height="194" transform="rotate(60)"/>
      <rect x="-97" y="-97" width="194" height="194" transform="rotate(75)"/>
    </g>
  </svg>
  <p class="offer-text">
    <span class="big">Free</span>
    <span class="small">initial<br>consultations<br>and advice.</span>
  </p>
</main>
</body>
</html>
```